Business Card Design Project

I need a business card designed from scratch. I have an existing logo that I can upload in Illustrator for modification or redesign.

The Company is called Rank Harbor http://rankharbor.com.au and we provide Search Engine Optimization services to Australian businesses. The current logo signifies an increase in visitors, profits etc...

There are no restrictions as to the redesign - colours, style etc are all open to change.

Cards will be full colour and one sided printed at http://www.printlorvex.com.au so check their requirements for file format and sizes etc.

I will expect all original files upon completion of project.

Target Market(s)

Any business with a web site looking to improve their search engine rankings

Industry/Entity Type

Business

Requirements
Must have
• I like modern, sleek designs. Clean, not fussy, uncluttered.

```html
<!DOCTYPE html>
<html lang="en">
<head>
<meta charset="utf-8">
<title>Rank Harbor – Business Cards</title>
<link rel="stylesheet" href="https://fonts.googleapis.com/css2?family=Quattrocento+Sans:wght@400;700&family=Arimo:wght@400&display=swap">
<style>
  :root {
    --page: #ffffff;
    --ink: #111111;
    --blue: #1a6fb0;
    --grey-band: #e0e0e0;
    --slate: #3f5560;
    --mist-band: #d9e0e7;
    --mist-text: #a3b4c0;
    --accent: #f39a2b;
    --white: #ffffff;
  }
  html, body {
    margin: 0;
    padding: 0;
    width: 1200px;
    height: 741px;
    overflow: hidden;
    background: var(--page);
  }
  .canvas {
    position: relative;
    width: 1200px;
    height: 741px;
  }
  .card {
    position: absolute;
    left: 347px;
    width: 511px;
    height: 284px;
    background: var(--white);
    box-shadow: 4px 5px 10px rgba(0,0,0,0.25);
    overflow: hidden;
    font-family: "Quattrocento Sans", sans-serif;
  }
  .card--classic { top: 45px; }
  .card--soft { top: 392px; }

  .card__head {
    position: absolute;
    left: 0; top: 0; right: 0;
    height: 86px;
    background: var(--white);
  }
  .card__band {
    position: absolute;
    left: 0; right: 0; top: 86px; bottom: 0;
  }
  .card--classic .card__band { background: var(--grey-band); }
  .card--soft .card__band { background: var(--mist-band); }

  .brand {
    position: absolute;
    display: flex;
    align-items: center;
    gap: 10px;
    white-space: nowrap;
  }
  .brand__dot {
    width: 14px; height: 14px;
    border-radius: 50%;
  }
  .card--classic .brand { left: 16px; top: 22px; }
  .card--classic .brand__name {
    font-size: 38px; font-weight: 700; color: var(--blue); line-height: 1;
  }
  .card--classic .brand__dot { background: var(--blue); }
  .card--soft .brand { left: 16px; top: 26px; }
  .card--soft .brand__name {
    font-size: 36px; font-weight: 400; color: var(--slate); line-height: 1;
  }
  .card--soft .brand__dot { background: var(--accent); }

  .tagline {
    position: absolute;
    font-family: "Arimo", sans-serif;
    letter-spacing: 1.6px;
    white-space: nowrap;
    margin: 0;
  }
  .card--classic .tagline { left: 17px; top: 14px; font-size: 18px; color: var(--white); }
  .card--soft .tagline { left: 21px; top: 12px; font-size: 19.5px; color: var(--mist-text); }

  .contact {
    position: absolute;
    left: 249px;
    top: 99px;
    margin: 0;
    font-style: normal;
    font-size: 13.5px;
    line-height: 17px;
    color: var(--ink);
  }
  .contact__label { font-weight: 700; margin-right: 4px; }
  .card--classic .contact__label { color: var(--blue); }
  .card--soft .contact__label { color: var(--white); }
</style>
</head>
<body>
<main class="canvas">

  <section class="card card--classic" aria-label="Business card, grey version">
    <header class="card__head">
      <div class="brand">
        <span class="brand__dot"></span>
        <span class="brand__name">Rank Harbor</span>
      </div>
    </header>
    <div class="card__band">
      <p class="tagline">RANKINGS FOR PROFIT</p>
      <address class="contact">
        15, Dummy Street,<br>
        Postcode, City. Australia<br>
        <span class="contact__label">t:</span> 1300 555 204<br>
        <span class="contact__label">e:</span> enquiry@rankharbor.com.au<br>
        <span class="contact__label">w:</span>www.rankharbor.com.au
      </address>
    </div>
  </section>

  <section class="card card--soft" aria-label="Business card, blue-grey version">
    <header class="card__head">
      <div class="brand">
        <span class="brand__dot"></span>
        <span class="brand__name">Rank Harbor</span>
      </div>
    </header>
    <div class="card__band">
      <p class="tagline">RANKINGS FOR PROFIT</p>
      <address class="contact">
        15, Dummy Street,<br>
        Postcode, City. Australia<br>
        <span class="contact__label">t:</span> 1300 555 204<br>
        <span class="contact__label">e:</span> enquiry@rankharbor.com.au<br>
        <span class="contact__label">w:</span>www.rankharbor.com.au
      </address>
    </div>
  </section>

</main>
</body>
</html>
```